New Business Card Design Project

We are a spa looking to create a professional elegant business card for a spa mainly black and white with a splash of lime green. This card will be two sided - the front side will have an image, the logo, and the spa's information - the back side will have a promotion for new customers - NEW CUSTOMERS $20 OFF

Look and feel: chic, modern, and spa-ish.
Information to be included:
Therapist Name
Therapist specialty
Address: 5174 Marlowe Ave, Beverly Hills CA 90211
Phone: (310) 482-3957

Let me know if you have any questions!

Thank you

Industry/Entity Type

Business

```html
<!DOCTYPE html>
<html lang="en">
<head>
<meta charset="utf-8">
<title>Linden Day Spa – Business Card</title>
<link href="https://fonts.googleapis.com/css2?family=Raleway:wght@400;500&display=swap" rel="stylesheet">
<style>
  :root {
    --backdrop: #3b2518;
    --card: #ffffff;
    --ink: #111111;
    --muted: #555555;
    --lime: #8ed61c;
    --lime-soft: rgba(142, 214, 28, 0);
  }
  html, body {
    margin: 0;
    padding: 0;
    width: 1200px;
    height: 1000px;
    overflow: hidden;
    background: var(--backdrop);
    font-family: "Raleway", Arial, sans-serif;
    color: var(--ink);
  }
  .canvas {
    position: relative;
    width: 1200px;
    height: 1000px;
  }
  .card {
    position: absolute;
    top: 171px;
    width: 374px;
    height: 655px;
    background: var(--card);
    overflow: hidden;
  }
  .card--front { left: 176px; }
  .card--back { left: 650px; }

  .foliage {
    position: absolute;
    display: block;
  }
  .foliage--top-right { right: 0; top: 0; width: 150px; height: 115px; }
  .foliage--mid-left { left: 0; top: 360px; width: 90px; height: 160px; }
  .foliage--top-left { left: 0; top: 0; width: 150px; height: 115px; }
  .foliage--mid-right { right: 0; top: 360px; width: 90px; height: 160px; }

  .line {
    position: absolute;
    left: 0;
    width: 100%;
    text-align: center;
    white-space: nowrap;
    line-height: 1;
    font-weight: 400;
  }
  .brand-name {
    top: 196px;
    font-size: 34px;
    font-weight: 500;
    letter-spacing: 1px;
    color: var(--ink);
  }
  .therapist-name { top: 374px; font-size: 35px; }
  .therapist-specialty { top: 415px; font-size: 13px; letter-spacing: 0.5px; color: var(--muted); text-transform: uppercase; }
  .contact { font-size: 19px; }
  .contact--street { top: 457px; }
  .contact--city { top: 481px; }
  .contact--label { top: 528px; }
  .contact--phone { top: 552px; }

  .offer-amount { top: 126px; font-size: 52px; }
  .offer-for { top: 184px; font-size: 26px; }
  .offer-audience { top: 224px; font-size: 40px; }
  .offer-terms { font-size: 19px; }
  .offer-terms--1 { top: 293px; }
  .offer-terms--2 { top: 319px; }
  .offer-terms--3 { top: 345px; }
  .fine-print { font-size: 15px; }
  .fine-print--1 { top: 479px; }
  .fine-print--2 { top: 505px; }
</style>
</head>
<body>
<div class="canvas">

  <section class="card card--front">
    <svg class="foliage foliage--top-right" role="img" aria-label="Lime green bamboo leaves" viewBox="0 0 150 115">
      <defs>
        <linearGradient id="leafFadeTR" x1="1" y1="0" x2="0" y2="1">
          <stop offset="0" stop-color="#8ed61c"/>
          <stop offset="1" stop-color="#8ed61c" stop-opacity="0.15"/>
        </linearGradient>
      </defs>
      <polygon points="150,0 150,115 0,85 105,0" fill="url(#leafFadeTR)"/>
    </svg>
    <svg class="foliage foliage--mid-left" role="img" aria-label="Lime green bamboo leaves" viewBox="0 0 90 160">
      <defs>
        <linearGradient id="leafFadeML" x1="0" y1="0" x2="1" y2="1">
          <stop offset="0" stop-color="#8ed61c"/>
          <stop offset="1" stop-color="#8ed61c" stop-opacity="0.15"/>
        </linearGradient>
      </defs>
      <polygon points="0,0 90,75 48,160 0,40" fill="url(#leafFadeML)"/>
    </svg>

    <div class="line brand-name">Linden Day Spa</div>

    <div class="line therapist-name">Clara Hale</div>
    <div class="line therapist-specialty">Therapist Specialty</div>

    <div class="line contact contact--street">5174 Marlowe Ave,</div>
    <div class="line contact contact--city">Beverly Hills CA 90211</div>
    <div class="line contact contact--label">Phone:</div>
    <div class="line contact contact--phone">(310) 482-3957</div>
  </section>

  <section class="card card--back">
    <svg class="foliage foliage--top-left" role="img" aria-label="Lime green bamboo leaves" viewBox="0 0 150 115">
      <defs>
        <linearGradient id="leafFadeTL" x1="0" y1="0" x2="1" y2="1">
          <stop offset="0" stop-color="#8ed61c"/>
          <stop offset="1" stop-color="#8ed61c" stop-opacity="0.15"/>
        </linearGradient>
      </defs>
      <polygon points="0,0 45,0 150,85 0,115" fill="url(#leafFadeTL)"/>
    </svg>
    <svg class="foliage foliage--mid-right" role="img" aria-label="Lime green bamboo leaves" viewBox="0 0 90 160">
      <defs>
        <linearGradient id="leafFadeMR" x1="1" y1="0" x2="0" y2="1">
          <stop offset="0" stop-color="#8ed61c"/>
          <stop offset="1" stop-color="#8ed61c" stop-opacity="0.15"/>
        </linearGradient>
      </defs>
      <polygon points="90,0 90,40 42,160 0,75" fill="url(#leafFadeMR)"/>
    </svg>

    <div class="line offer-amount">20% OFF</div>
    <div class="line offer-for">for</div>
    <div class="line offer-audience">New Clients</div>

    <div class="line offer-terms offer-terms--1">Good for first visit.</div>
    <div class="line offer-terms offer-terms--2">Receive 20% off of one</div>
    <div class="line offer-terms offer-terms--3">service or one product.</div>

    <div class="line fine-print fine-print--1">Please call to make an appointment.</div>
    <div class="line fine-print fine-print--2">May not be redeemed for cash.</div>
  </section>

</div>
</body>
</html>
```